Verdant Loop Advisors, LLC

I am looking for a simple, clear layout with my logo prominent and embossed, on the best quality card stock available. I would like the business name and phone number included on the card as well......I dont want my name anywhere on the card and I would like my logo embossed on the card......something simple with a white back......open to designs as long as they go along with recycling symbols and green type stuff.....The address, website, cell number, fax number, and email are listed below

5374 Tillbury Fenwood Road
Brackenfield, MD 20999

c. 240.555.0143 f. 240.555.0187
e. sales@verdantloopadvisors.example
w. www.verdantloopadvisors.example

Industry/Entity Type

Recycling

```html
<!DOCTYPE html>
<html lang="en">
<head>
<meta charset="utf-8">
<title>Verdant Loop Advisors, LLC — Business Cards</title>
<link rel="stylesheet" href="https://fonts.googleapis.com/css2?family=Open+Sans:wght@400;700&display=swap">
<style>
  :root {
    --backdrop: #e9e9e9;
    --card: #f7f7f7;
    --ink: #2a2116;
    --text: #333333;
    --green: #1f7a36;
    --card-shadow: rgba(0, 0, 0, 0.12);
  }
  * { box-sizing: border-box; margin: 0; padding: 0; }
  html, body {
    width: 1200px;
    height: 952px;
    overflow: hidden;
    background: var(--backdrop);
    font-family: "Open Sans", Arial, sans-serif;
  }
  .canvas { position: relative; width: 1200px; height: 952px; }
  .card {
    position: absolute;
    width: 560px;
    height: 320px;
    background: var(--card);
    box-shadow: 0 6px 18px var(--card-shadow);
    color: var(--text);
    overflow: hidden;
  }
  .card--wide { left: 560px; top: 90px; }
  .card--stacked { left: 90px; top: 520px; }

  .brand { display: flex; align-items: center; justify-content: center; gap: 14px; }
  .brand__mark {
    width: 44px; height: 44px;
    background: var(--green);
    flex: none;
  }
  .brand__name {
    font-weight: 700;
    color: var(--ink);
    letter-spacing: 0.5px;
    line-height: 1.1;
    white-space: nowrap;
  }

  .card--wide .brand { position: absolute; left: 0; right: 0; top: 80px; }
  .card--wide .brand__name { font-size: 26px; }

  .card--stacked .brand {
    position: absolute; left: 0; right: 0; top: 48px;
    flex-direction: column; gap: 16px;
  }
  .card--stacked .brand__mark { width: 100px; height: 100px; }
  .card--stacked .brand__name { font-size: 26px; text-align: center; }

  .contact {
    position: absolute;
    left: 0; right: 0;
    font-size: 12.5px;
    font-style: normal;
    line-height: 1.45;
    text-align: center;
  }
  .card--wide .contact { top: 180px; }
  .card--stacked .contact { top: 232px; }
  .contact__label { color: var(--green); margin-right: 4px; }
  .contact__item + .contact__label { margin-left: 8px; }
</style>
</head>
<body>
<main class="canvas">
  <section class="card card--wide" aria-label="Business card, horizontal layout">
    <div class="brand">
      <span class="brand__mark" aria-hidden="true"></span>
      <span class="brand__name">Verdant Loop Advisors, LLC</span>
    </div>
    <address class="contact">
      <div><span class="contact__label">a</span><span class="contact__item">5374 Tillbury Fenwood Road, Brackenfield, MD 20999</span></div>
      <div><span class="contact__label">c</span><span class="contact__item">240.555.0143</span><span class="contact__label">f</span><span class="contact__item">240.555.0187</span><span class="contact__label">e</span><span class="contact__item">sales@verdantloopadvisors.example</span></div>
      <div><span class="contact__label">w</span><span class="contact__item">www.verdantloopadvisors.example</span></div>
    </address>
  </section>

  <section class="card card--stacked" aria-label="Business card, stacked layout">
    <div class="brand">
      <span class="brand__mark" aria-hidden="true"></span>
      <span class="brand__name">Verdant Loop Advisors, LLC</span>
    </div>
    <address class="contact">
      <div><span class="contact__label">a</span><span class="contact__item">5374 Tillbury Fenwood Road, Brackenfield, MD 20999</span></div>
      <div><span class="contact__label">c</span><span class="contact__item">240.555.0143</span><span class="contact__label">f</span><span class="contact__item">240.555.0187</span><span class="contact__label">e</span><span class="contact__item">sales@verdantloopadvisors.example</span></div>
      <div><span class="contact__label">w</span><span class="contact__item">www.verdantloopadvisors.example</span></div>
    </address>
  </section>
</main>
</body>
</html>
```